I need a cd cover for a new pop rock album called "Letters from the tin harbour"
The main color of the artwork shall obviously be orange. The artwork shouldn't be too "obvious", but it would be better something a bit abstract.
Please remember that it is a Music Cd Cover, so do not send business logo or advertisement images.

It's a pop rock album, so the target customers are young and adult people from 15-60 years old

• Orange as main colour
The Artist name is: Tomas Verhelst
The Title: Letters from the tin harbour
• Not too cheesy or dreamy images please. No simple sunset or sunrise pics

```html
<!DOCTYPE html>
<html lang="en">
<head>
<meta charset="utf-8">
<title>Letters from the Tin Harbour – CD Cover</title>
<link rel="stylesheet" href="https://fonts.googleapis.com/css2?family=Fredoka:wght@600;700&display=swap">
<style>
  :root {
    --page: #ffffff;
    --back-orange: #dc9f56;
    --back-orange-deep: #c98a42;
    --front-orange: #e3a35c;
    --front-orange-deep: #d08d46;
    --bright-orange: #f9a845;
    --ink: #111111;
  }
  html, body {
    margin: 0;
    padding: 0;
    width: 1200px;
    height: 698px;
    overflow: hidden;
    background: var(--page);
  }
  .canvas {
    position: relative;
    width: 1200px;
    height: 698px;
    font-family: "Fredoka", "Arial Rounded MT Bold", sans-serif;
    color: var(--ink);
  }
  .back-cover {
    position: absolute;
    left: 34px;
    top: 53px;
    width: 602px;
    height: 503px;
    overflow: hidden;
  }
  .back-artwork {
    position: absolute;
    inset: 0;
    background: radial-gradient(ellipse at 60% 55%, var(--back-orange-deep) 0%, var(--back-orange) 55%, #e0a75e 100%);
  }
  .back-title {
    position: absolute;
    left: 0;
    width: 588px;
    top: 32px;
    margin: 0;
    text-align: center;
    font-weight: 600;
    font-size: 29px;
    line-height: 1.42;
  }
  .back-artist {
    position: absolute;
    left: 0;
    width: 588px;
    top: 438px;
    margin: 0;
    text-align: center;
    font-weight: 600;
    font-size: 19px;
  }
  .spine-text {
    position: absolute;
    left: 609px;
    top: 76px;
    width: 26px;
    height: 444px;
    margin: 0;
    writing-mode: vertical-rl;
    transform: rotate(180deg);
    font-weight: 600;
    font-size: 19px;
    line-height: 26px;
    white-space: nowrap;
  }
  .spine-text .spine-title { margin-bottom: 22px; }
  .front-cover {
    position: absolute;
    left: 636px;
    top: 46px;
    width: 517px;
    height: 514px;
    overflow: hidden;
  }
  .front-artwork {
    position: absolute;
    inset: 0;
    background: linear-gradient(160deg, var(--front-orange) 0%, var(--front-orange-deep) 60%, var(--front-orange) 100%);
  }
  .front-highlight {
    position: absolute;
    left: 0;
    top: 0;
    width: 517px;
    height: 514px;
  }
  .front-title {
    position: absolute;
    right: 24px;
    top: -14px;
    margin: 0;
    text-align: right;
    font-weight: 700;
    font-size: 76px;
    line-height: 104px;
    letter-spacing: 0.5px;
  }
  .front-title span { display: block; }
</style>
</head>
<body>
<div class="canvas">
  <section class="back-cover">
    <div class="back-artwork" role="img" aria-label="Abstract close-up of orange liquid with foam and bubbles"></div>
    <h2 class="back-title">Letters from the Tin<br>Harbour</h2>
    <p class="back-artist">Tomas Verhelst</p>
  </section>

  <p class="spine-text"><span class="spine-title">Letters from the Tin Harbour</span><span class="spine-artist">Tomas Verhelst</span></p>

  <section class="front-cover">
    <div class="front-artwork" role="img" aria-label="Abstract close-up of orange liquid with foam and bubbles"></div>
    <svg class="front-highlight" viewBox="0 0 517 514" aria-hidden="true">
      <path fill="var(--bright-orange)" d="M0 0 H517 V118 C500 110 470 96 440 108 C410 118 380 132 345 125 C320 120 300 130 290 150 C282 175 270 200 250 220 C225 240 200 250 170 245 C150 240 140 225 130 210 C118 195 100 190 92 175 C85 160 80 150 60 145 C40 140 20 150 0 140 Z"/>
      <path fill="var(--front-orange)" d="M10 12 C30 2 60 4 80 14 C95 22 110 20 125 30 C135 40 120 52 100 55 C80 58 55 50 35 45 C20 40 5 30 10 12 Z"/>
    </svg>
    <h1 class="front-title">
      <span>LETTERS</span>
      <span>FROM</span>
      <span>THE</span>
      <span>TIN</span>
      <span>HARBOUR</span>
    </h1>
  </section>
</div>
</body>
</html>
```